Copper Meadow Dental Lab - Presentation Folder Design

1. We are a dental lab providing a full range of dental products to restore and enhance the natural beauty of the patients’ smiles. We provide fixed restorations (Full-Contour Solid Zirconia, KRT o.lumo, Dune Prime, Full Cast, PFM, Temporary Crowns, Diagnostic Wax-Ups and Study Models), implant restorations (Single and Multi Tooth Restorations, Zirconia Prosthesis, Full Arch Hybrid Prosthesis), and
removable restorations (Dentures and Partials, PolyBend, Kernalite).
2. The target market are dentists, oral surgeons, implant manufacturers, and etc. We are not targeting patients.
3. Design specifics - no specifics, but I have provided our logo for reference if needed

Target Market(s)

Dentists, Oral Surgeons, implant manufacturers

Industry/Entity Type

Dental

Requirements
Must have
• Name - Copper Meadow Dental Lab, address - 4126 Orchard Ln, Suite 310, Annandale, VA 22003, office number - 703-555-0142, fax number - 703-555-0143, email - info@cmdentalworks.example

```html
<!DOCTYPE html>
<html lang="en">
<head>
<meta charset="utf-8">
<title>Copper Meadow Dental Lab – Presentation Folder</title>
<link rel="stylesheet" href="https://fonts.googleapis.com/css2?family=Montserrat:wght@300;400;500;600;700;800&display=swap">
<style>
  :root{
    --stage:#d9d9de;
    --paper:#ffffff;
    --navy:#0d3a7a;
    --royal:#0a63b8;
    --deep:#103f86;
    --ink:#1e1e24;
    --brand:#2e3192;
    --white:#ffffff;
  }
  *{margin:0;padding:0;box-sizing:border-box}
  html,body{width:848px;height:1200px;overflow:hidden;background:var(--stage)}
  body{font-family:"Montserrat",sans-serif;position:relative}
  .folder{
    position:absolute;left:24px;top:317px;width:800px;height:566px;
    display:flex;background:var(--paper);
    box-shadow:0 2px 6px rgba(0,0,0,.18);
  }
  .panel{position:relative;width:400px;height:100%;overflow:hidden}

  /* back panel */
  .back-photo{
    position:absolute;left:0;top:0;width:400px;height:170px;
    background:linear-gradient(180deg,#c9d3e2 0%,#dfe5ee 55%,#ffffff 100%);
  }
  .services{
    position:absolute;left:40px;top:180px;width:320px;padding:14px 0;
    font-size:7.6px;line-height:11.6px;text-align:center;color:var(--ink);
  }
  .services::before,.services::after{
    content:"";position:absolute;left:20px;right:20px;height:4px;
    background:radial-gradient(ellipse at center,rgba(0,0,0,.13) 0%,rgba(0,0,0,0) 70%);
  }
  .services::before{top:0}
  .services::after{bottom:0}
  .back-name{
    position:absolute;left:0;width:400px;top:318px;text-align:center;
    font-size:15px;line-height:20px;font-weight:600;color:var(--brand);letter-spacing:.5px;
  }
  .contact-band{
    position:absolute;left:0;bottom:0;width:400px;height:141px;
    background:linear-gradient(100deg,var(--navy) 0%,var(--deep) 45%,var(--royal) 100%);
    color:var(--white);text-align:center;font-size:7.6px;line-height:11.4px;padding-top:23px;
  }
  .contact-band p+p{margin-top:11px}
  .contact-band strong{font-weight:700}

  /* front panel */
  .front-photo{
    position:absolute;left:0;top:0;width:400px;height:425px;
    background:
      radial-gradient(ellipse 55% 40% at 35% 62%,rgba(160,200,245,.55) 0%,rgba(160,200,245,0) 100%),
      linear-gradient(160deg,#0d3f88 0%,#0b58b0 45%,#1573cc 70%,#0d3c82 100%);
  }
  .tagline{
    position:absolute;left:49px;top:22px;
    font-size:16px;line-height:21.5px;font-weight:300;color:var(--white);
  }
  .tagline::before{
    content:"";position:absolute;left:-17px;top:4px;width:2px;height:56px;background:var(--white);
  }
  .smiles{position:absolute;right:4px;top:0;width:96px;height:425px}
  .front-name{
    position:absolute;left:24px;top:455px;width:230px;text-align:center;
    font-size:17px;line-height:22px;font-weight:600;color:var(--brand);letter-spacing:.5px;
  }
  .front-web{
    position:absolute;right:32px;top:530px;
    font-size:7px;letter-spacing:1.3px;color:var(--brand);
  }
</style>
</head>
<body>
  <main class="folder">
    <section class="panel back">
      <div class="back-photo" role="img" aria-label="Dental technician in lab coat and glasses working on a model in an articulator, fading to white"></div>
      <p class="services">We provide fixed restorations (Full-Contour Solid Zirconia, KRT o.lumo, Dune Prime, Full Cast, PFM, Temporary Crowns, Diagnostic Wax-Ups and Study Models), implant restorations (Single and Multi Tooth Restorations, Zirconia Prosthesis, Full Arch Hybrid Prosthesis), and removable restorations (Dentures and Partials, PolyBend, Kernalite).</p>
      <div class="back-name">Copper Meadow<br>Dental Lab</div>
      <div class="contact-band">
        <p><strong>Copper Meadow Dental Lab</strong><br>4126 Orchard Ln, Suite 310, Annandale, VA 22003</p>
        <p>Office number - 703-555-0142<br>Fax number - 703-555-0143</p>
        <p>email - info@cmdentalworks.example<br><strong>www.cmdentalworks.example</strong></p>
      </div>
    </section>
    <section class="panel front">
      <div class="front-photo" role="img" aria-label="Gloved hands holding a dental instrument over a lab bench, tinted blue"></div>
      <p class="tagline">Restore and enhance<br>the natural beauty<br>of the patients’</p>
      <svg class="smiles" viewBox="0 0 96 425" aria-label="SMILES">
        <text transform="translate(93 425) rotate(-90)" font-family="Montserrat, sans-serif" font-weight="800" font-size="124" fill="#ffffff" textLength="425" lengthAdjust="spacingAndGlyphs">SMILES</text>
      </svg>
      <div class="front-name">Copper Meadow<br>Dental Lab</div>
      <div class="front-web">WWW.CMDENTALWORKS.EXAMPLE</div>
    </section>
  </main>
</body>
</html>
```